New website for selling opensource software business to business

Website K7 Software

The open source software industry has grown enormously in recent years. More and more customers from software companies choose an open source solution. K7 Software is going to fulfill this increasing demand.

Core business

Reselling software subcriptions (business to business).

Side business

Selling consultancy and Training to customers

Goals:

- Binding of customers to K7 IT Group
- Sales of subscriptions to customer
- Enlarge network K7 IT Group
- USP: Sales of complete package, Software, consultancy and training

Products

There are a couple of products/ services that K7 will provide. Below you will find an overview of the Products:

- Bluefen subscriptions
- Cratel subscriptions
- Velmor products
- Customized consultancy for the customer
- Customized training for the customer

Style

Behind the website should be a cms system like wordpress.

Target Market(s)

Business - Business

Industry/Entity Type

Business

Coding

Coded - Design and coding required

Number of Pages Required

5+ page

Font styles to use
Other font styles liked:
• Calibri

Colors
0355a3
3176b5
85abd2

Requirements
Must have
• Home page with large photo background, About us, contact page with safe option to request more info
• Portfolio pages:
• 4 pages with a product group each:
• 1. Blue fen
• 2. Crates
• 3. Velmor
• 4. Trustwardly
• 1. Blue Fen
• On top space for short info/bullets about Blue fen. Further, a grid with 8 columns. In the columns 2 buttons both lead to a popup. A popup for information and a popup for requesting a quote.
• 2. Cratel:
• On top space for short info/bullets about Cratel. Further, a grid with 3 columns. In the columns 2 buttons both lead to a popup. A popup for information and a popup for requesting a quote.
• 1. Velmor:
• On top space for short info/bullets about Velmor. Further, a grid with 4 columns. In the columns 2 buttons both lead to a popup. A popup for information and a popup for requesting a quote.
• 2. Trustwardly:
• On top space for short info/bullets about Trustwardly. Further, a grid with 2 columns. In the columns 2 buttons both lead to a popup. A popup for information and a popup for requesting a quote.

```html
<!DOCTYPE html>
<html lang="en">
<head>
<meta charset="utf-8">
<title>K7 Software – Open Source Software</title>
<link href="https://fonts.googleapis.com/css2?family=Poppins:wght@400;500;600;700&family=Open+Sans:wght@400;600;700&display=swap" rel="stylesheet">
<style>
:root{
  --brand-dark:#0355a3;
  --brand-mid:#3176b5;
  --brand-light:#85abd2;
  --ink:#222;
  --text:#444;
  --purple:#3d2a8c;
  --footer-bg:#f5f5f5;
  --line:#e2e2e2;
  --white:#fff;
}
*{box-sizing:border-box;margin:0;padding:0}
html,body{width:1120px;height:1200px;overflow:hidden;background:var(--white)}
body{position:relative;font-family:"Open Sans",sans-serif;color:var(--text)}
.site-header{position:absolute;left:0;top:0;width:1120px;height:87px;background:var(--white);z-index:5}
.brand-badge{position:absolute;left:92px;top:10px;width:152px;height:152px;border-radius:50%;background:#ececf0;border:5px solid var(--white);box-shadow:0 3px 10px rgba(0,0,0,.25);display:flex;align-items:center;justify-content:center;z-index:6}
.brand-name{font-family:"Poppins",sans-serif;font-weight:600;font-size:19px;color:var(--brand-dark);text-align:center;line-height:1.15}
.main-nav{position:absolute;left:394px;top:30px;display:flex;gap:29px;font-family:"Poppins",sans-serif;font-size:17px;color:var(--ink)}
.main-nav .has-menu::after{content:"";display:inline-block;margin-left:8px;border:4px solid transparent;border-top:5px solid var(--ink);vertical-align:1px}
.header-phone{position:absolute;left:766px;top:29px;display:flex;align-items:center;gap:10px;font-family:"Poppins",sans-serif;font-size:17px;color:var(--purple);letter-spacing:.5px}
.header-phone .icon{width:25px;height:25px;border-radius:50%;background:var(--purple);display:flex;align-items:center;justify-content:center}
.trial-btn{position:absolute;left:941px;top:29px;width:84px;height:28px;background:var(--brand-mid);border:1px solid var(--brand-dark);border-radius:3px;color:var(--white);font-family:"Poppins",sans-serif;font-weight:500;font-size:12px;display:flex;align-items:center;justify-content:center}
.hero{position:absolute;left:0;top:87px;width:1120px;height:533px;background:linear-gradient(180deg,#6b6358 0%,#4e453d 40%,#5a3a26 75%,#3d2a20 100%)}
.hero-title{position:absolute;left:0;top:230px;width:100%;text-align:center;font-family:"Poppins",sans-serif;color:var(--white);text-shadow:0 2px 6px rgba(0,0,0,.5)}
.hero-title h1{font-size:54px;font-weight:600;line-height:1;letter-spacing:1px}
.hero-title p{font-size:40px;font-weight:600;line-height:1.1;margin-top:-2px}
.hero-arrow{position:absolute;top:248px}
.products{position:absolute;left:0;top:620px;width:1120px;height:238px;background:linear-gradient(135deg,var(--brand-light) 0%,var(--brand-mid) 55%,#5a95cc 100%)}
.product-card{position:absolute;top:582px;width:216px;height:215px;background:var(--white);box-shadow:0 1px 4px rgba(0,0,0,.2);text-align:center;padding:0 10px}
.product-name{height:90px;display:flex;align-items:center;justify-content:center;gap:8px;font-family:"Poppins",sans-serif;font-weight:600;font-size:25px;color:var(--ink)}
.product-name .dot{width:24px;height:24px;border-radius:50%;background:var(--brand-mid)}
.product-card p{font-size:11px;line-height:21px;color:var(--text)}
.read-more{display:block;margin-top:8px;font-size:12.5px;color:var(--brand-mid)}
.info-band{position:absolute;left:0;top:858px;width:1120px;height:247px;background:var(--footer-bg);border-bottom:1px solid var(--line)}
.info-band .divider{position:absolute;top:0;width:1px;height:247px;background:var(--line)}
.contact h2,.newsletter h2{font-family:"Poppins",sans-serif;font-weight:500;font-size:19px;color:var(--ink);letter-spacing:.3px}
.contact{position:absolute;left:90px;top:58px}
.contact ul{list-style:none;margin-top:16px;font-size:12px;color:#333;line-height:19px}
.contact li{display:flex;gap:12px;margin-bottom:12px}
.contact svg{flex:none;margin-top:2px}
.footer-badge{position:absolute;left:447px;top:52px;width:162px;height:162px;border-radius:50%;background:#e6e6ea;display:flex;align-items:center;justify-content:center}
.footer-badge .brand-name{font-size:21px}
.newsletter{position:absolute;right:95px;top:52px;text-align:right;width:300px}
.newsletter p{margin-top:12px;font-size:11px;line-height:18px;color:#333}
.signup{position:absolute;right:93px;top:148px;width:283px;height:39px;border:1px solid #ddd;background:var(--white);display:flex}
.signup span{flex:1;padding-left:13px;font-size:11px;color:#555;line-height:37px}
.signup b{width:90px;background:var(--brand-dark);color:var(--white);font-family:"Poppins",sans-serif;font-weight:600;font-size:14px;display:flex;align-items:center;justify-content:center}
.site-footer{position:absolute;left:0;top:1105px;width:1120px;height:95px;text-align:center;font-size:10.5px;color:#333}
.site-footer nav{margin-top:35px}
.site-footer nav span{margin:0 6px;color:#666}
.site-footer p{margin-top:15px}
</style>
</head>
<body>
<header class="site-header">
  <nav class="main-nav">
    <span>Home</span><span>About us</span><span class="has-menu">Portfolio</span><span>Contact</span>
  </nav>
  <div class="header-phone">
    <span class="icon"><svg width="13" height="13" viewBox="0 0 24 24"><path fill="#fff" d="M6.6 10.8a15 15 0 006.6 6.6l2.2-2.2a1 1 0 011-.25 11.4 11.4 0 003.6.57 1 1 0 011 1V20a1 1 0 01-1 1A17 17 0 013 4a1 1 0 011-1h3.5a1 1 0 011 1c0 1.25.2 2.45.57 3.57a1 1 0 01-.25 1z"/></svg></span>
    888-555-0147
  </div>
  <div class="trial-btn">FREE TRIAL</div>
</header>
<div class="brand-badge"><span class="brand-name">K7<br>Software</span></div>

<section class="hero" role="img" aria-label="Photo of a bright open-plan office with developers working at laptops">
  <svg class="hero-arrow" style="left:68px" width="26" height="48" viewBox="0 0 26 48"><path d="M24 2L3 24l21 22" fill="none" stroke="#fff" stroke-width="2.5"/></svg>
  <svg class="hero-arrow" style="left:1026px" width="26" height="48" viewBox="0 0 26 48"><path d="M2 2l21 22L2 46" fill="none" stroke="#fff" stroke-width="2.5"/></svg>
  <div class="hero-title">
    <h1>K7 SOFTWARE</h1>
    <p>Open Source Software</p>
  </div>
</section>

<section class="products"></section>
<article class="product-card" style="left:92px">
  <div class="product-name"><span class="dot"></span>Bluefen</div>
  <p>Sed ut perspiciatis unde omnis iste natus error sit voluptatem accusantium doloremque laudantium, totam rem aperiam, eaque ipsa</p>
  <span class="read-more">[ READ MORE ]</span>
</article>
<article class="product-card" style="left:332px">
  <div class="product-name"><span class="dot"></span>Cratel</div>
  <p>Sed ut perspiciatis unde omnis iste natus error sit voluptatem accusantium doloremque laudantium, totam rem aperiam, eaque ipsa quae</p>
  <span class="read-more">[ READ MORE ]</span>
</article>
<article class="product-card" style="left:570px">
  <div class="product-name">Velmor</div>
  <p>Sed ut perspiciatis unde omnis iste natus error sit voluptatem accusantium doloremque laudantium, totam rem aperiam, eaque ipsa quae</p>
  <span class="read-more">[ READ MORE ]</span>
</article>
<article class="product-card" style="left:810px">
  <div class="product-name" style="font-size:21px"><span class="dot"></span>Trustwardly</div>
  <p>Sed ut perspiciatis unde omnis iste natus error sit voluptatem accusantium doloremque laudantium, totam rem aperiam, eaque ipsa quae</p>
  <span class="read-more">[ READ MORE ]</span>
</article>

<section class="info-band">
  <span class="divider" style="left:400px"></span>
  <span class="divider" style="left:656px"></span>
  <div class="contact">
    <h2>CONTACT US</h2>
    <ul>
      <li><svg width="13" height="16" viewBox="0 0 24 30"><path d="M12 1a10 10 0 00-10 10c0 7 10 18 10 18s10-11 10-18A10 10 0 0012 1z" fill="none" stroke="#333" stroke-width="3"/><circle cx="12" cy="11" r="3.5" fill="#333"/></svg><span>K7 Software, Suite 410 Harbor Vale<br>CA 90417</span></li>
      <li><svg width="13" height="13" viewBox="0 0 24 24"><path fill="#333" d="M6.6 10.8a15 15 0 006.6 6.6l2.2-2.2a1 1 0 011-.25 11.4 11.4 0 003.6.57 1 1 0 011 1V20a1 1 0 01-1 1A17 17 0 013 4a1 1 0 011-1h3.5a1 1 0 011 1c0 1.25.2 2.45.57 3.57a1 1 0 01-.25 1z"/></svg><span style="font-size:13px">Phone: (310) 555-0192</span></li>
      <li><svg width="13" height="13" viewBox="0 0 24 24"><path fill="#333" d="M2 5h20v14H2z"/><path d="M2 5l10 8 10-8" fill="none" stroke="#f5f5f5" stroke-width="2"/></svg><span>Email: Support@K7Software.com</span></li>
    </ul>
  </div>
  <div class="footer-badge"><span class="brand-name">K7<br>Software</span></div>
  <div class="newsletter">
    <h2>SIGN UP FOR NEWSLETTER</h2>
    <p>Excepteur sint occaecat cupidatat non proident, sunt in<br>culpa qui officia deserunt</p>
  </div>
  <div class="signup"><span>Enter email</span><b>SIGN UP</b></div>
</section>

<footer class="site-footer">
  <nav>Home<span>|</span>Portfolio<span>|</span>About us<span>|</span>Terms Of Service<span>|</span>Contact</nav>
  <p>©2017 K7 Software. All Rights Reserved.</p>
</footer>
</body>
</html>
```